Business Card

Just need business logo with phone number on it. 0472 318 506
And the following on the bottom of the card.

"Your local plumbing experts".
and emblems for kovo card, cheque and cash

```html
<!DOCTYPE html>
<html lang="en">
<head>
<meta charset="utf-8">
<title>East Ridge Plumbing &amp; Drainage – Business Card</title>
<link rel="stylesheet" href="https://fonts.googleapis.com/css2?family=Orbitron:wght@700;900&display=swap">
<style>
  :root {
    --brand-red: #e31e24;
    --brand-blue: #1a7cc1;
    --card-white: #f4f5f7;
    --stage: #d9dadc;
    --ink-light: #ffffff;
  }
  * { margin: 0; padding: 0; box-sizing: border-box; }
  html, body {
    width: 1200px;
    height: 800px;
    overflow: hidden;
    background: var(--stage);
  }
  .business-card {
    position: absolute;
    left: 110px;
    top: 100px;
    width: 980px;
    height: 600px;
    background: var(--card-white);
    overflow: hidden;
    font-family: "Orbitron", sans-serif;
    box-shadow: 0 6px 24px rgba(0,0,0,0.12);
  }
  .brand-name {
    position: absolute;
    left: 96px;
    top: 92px;
    color: var(--brand-red);
    font-weight: 900;
    line-height: 1;
  }
  .brand-name .name-main {
    display: flex;
    align-items: center;
    gap: 22px;
    font-size: 92px;
    letter-spacing: 2px;
  }
  .brand-name .name-mark {
    width: 40px;
    height: 40px;
    border-radius: 50%;
    background: var(--brand-red);
  }
  .brand-name .name-sub {
    display: block;
    margin-top: 14px;
    font-size: 39px;
    letter-spacing: 9px;
  }
  .phone-number {
    position: absolute;
    left: 96px;
    top: 300px;
    color: var(--brand-red);
    font-weight: 900;
    font-size: 64px;
    letter-spacing: 5px;
  }
  .footer-band {
    position: absolute;
    left: 0;
    bottom: 0;
    width: 980px;
    height: 130px;
  }
  .tagline {
    position: absolute;
    left: 40px;
    top: 516px;
    color: var(--ink-light);
    font-weight: 700;
    font-size: 21px;
    letter-spacing: 2px;
    white-space: nowrap;
  }
  .payment-options {
    position: absolute;
    right: 30px;
    top: 500px;
    display: flex;
    align-items: center;
    gap: 14px;
    color: var(--brand-blue);
    font-weight: 900;
  }
  .payment-options .pay-card {
    font-size: 32px;
    letter-spacing: 2px;
  }
  .payment-options .pay-divider {
    width: 2px;
    height: 46px;
    background: var(--brand-blue);
  }
  .payment-options .pay-other {
    font-size: 18px;
    line-height: 1.05;
    letter-spacing: 1px;
  }
</style>
</head>
<body>
  <div class="business-card">
    <svg class="footer-band" viewBox="0 0 980 130" aria-hidden="true">
      <path d="M0 0 H980 V130 H0 Z" fill="var(--brand-red)"/>
      <path d="M620 0 Q655 0 660 20 L670 60 Q680 96 720 96 H980 V0 Z" fill="var(--card-white)"/>
    </svg>

    <h1 class="brand-name">
      <span class="name-main">EAST RIDGE <span class="name-mark"></span></span>
      <span class="name-sub">PLUMBING &amp; DRAINAGE</span>
    </h1>

    <p class="phone-number">0472 318 506</p>

    <p class="tagline">YOUR LOCAL PLUMBING EXPERTS</p>

    <div class="payment-options">
      <span class="pay-card">KOVO</span>
      <span class="pay-divider"></span>
      <span class="pay-other">CHEQUE<br>&amp; CASH</span>
    </div>
  </div>
</body>
</html>
```